Wohnhof am Weiher - Zeitungsinserat für den Verkauf von Eigentumswohnungen

Wir brauchen ein Zeitungsinserat in zwei Formaten. Einmal 296 Breite x 440 Höhe mm und einmal 296 Breite x 220 mm Höhe.
Als Basis dient der sehr grobe Entwurf im Powerpoint (Entwurf.pptx).
Auf dem Entwurf fehlen noch die Kontaktangeben:
Brunnhofer Liegenschaften AG
Seematteweg 14
4387 Tannried
079 462 37 58
rbrunnhofer@tessin-ostwald.ch

Zudem muss noch der Link auf die Webseite aufgeführt werden.
www.wohnhof-am-weiher.ch

Zudem fehlt noch der Text:
Fordern Sie noch heute die Verkaufsunterlagen gedruckt oder per Email an. Schreiben Sie uns einfach eine Chatpost mit Ihrer Adresse.

Ich habe noch Files von den Innenvisualisierungen, den Aussenvisualisierungen sowie unser Logo hinzugefügt. Zudem habe ich Ihnen die Verkaufsbrochure angefügt. Sie können die Daten vom Entwurf gerne ergänzen wenn Ihnen etwas gefällt. Schön wäre es, wenn Sie den Stil ähnlich machen würden wie die Brochure.

Target Market(s)

Famillien, Paare und Rentner

Font styles to use
Serif

Colors

Designer to choose colors to be used in the design.

Requirements
Must have
• Tolles Design das sofort anspricht!

```html
<!DOCTYPE html>
<html lang="de">
<head>
<meta charset="utf-8">
<title>Wohnhof am Weiher – Inserat</title>
<link rel="stylesheet" href="https://fonts.googleapis.com/css2?family=Montserrat:wght@600;800;900&family=Arimo:ital,wght@0,400;0,700;1,700&display=swap">
<style>
  :root{
    --blue:#1b6d91;
    --red:#e3232b;
    --panel:#e9e9ea;
    --band:#c8d5df;
    --page:#f1f2f4;
    --cell:#dcdcde;
    --cell-alt:#e6e6e8;
    --ink:#222;
    --white:#fff;
  }
  *{box-sizing:border-box;margin:0;padding:0}
  html,body{width:1200px;height:807px;overflow:hidden;background:var(--page)}
  body{font-family:"Arimo",Arial,sans-serif;color:var(--ink);position:relative}

  .hero{position:absolute;left:0;top:0;width:763px;height:432px;
    background:
      linear-gradient(90deg,rgba(196,70,50,.75) 0%,rgba(196,70,50,.25) 25%,rgba(0,0,0,0) 45%),
      linear-gradient(180deg,#8fb3d6 0%,#c9dbe9 35%,#d8dcd6 52%,#8fa58a 62%,#6f9152 75%,#5d7f3f 100%);}
  .hero-title{position:absolute;left:54px;top:232px;font-family:"Montserrat",sans-serif;font-weight:900;
    color:var(--white);font-size:74px;line-height:.98;letter-spacing:-1px;text-transform:uppercase}
  .hero-sub{position:absolute;left:52px;top:381px;width:428px;height:20px;background:var(--red);
    color:var(--white);font-family:"Montserrat",sans-serif;font-weight:600;font-size:15px;line-height:20px;padding-left:8px}

  .info{position:absolute;left:763px;top:0;width:437px;height:432px;background:var(--panel)}
  .brand{position:absolute;left:84px;top:62px;display:flex;align-items:center;gap:12px}
  .brand-mark{width:14px;height:14px;background:var(--blue)}
  .brand-name{font-family:"Montserrat",sans-serif;font-weight:600;color:var(--blue);font-size:21px;line-height:1.1;letter-spacing:1px}
  .features{position:absolute;left:28px;top:158px;display:grid;grid-template-columns:188px 188px;column-gap:12px}
  .feature{position:relative;padding-left:18px;margin-bottom:10px}
  .feature::before{content:"";position:absolute;left:0;top:3px;width:7px;height:7px;background:var(--red)}
  .feature h3{font-size:11px;font-weight:700;color:var(--blue);margin-bottom:2px}
  .feature p{font-size:8px;line-height:1.42;color:#333}
  .divider{position:absolute;left:35px;top:390px;width:378px;height:1px;background:#e07a70}
  .cta{position:absolute;left:30px;top:400px;width:390px;text-align:center;font-size:8px;line-height:1.5;font-style:italic;font-weight:700;color:#333}

  .band{position:absolute;left:0;top:432px;width:1200px;height:38px;background:var(--band)}

  .house{position:absolute;top:462px;width:355px}
  .house-a{left:48px}.house-b{left:422px}.house-c{left:797px}
  .house-accent{position:absolute;top:0;width:128px;height:7px;background:var(--red)}
  .house-a .house-accent{left:0}.house-b .house-accent{left:98px}.house-c .house-accent{right:0}
  .house-head{margin-top:7px;height:36px;background:var(--blue);color:var(--white);text-align:center;
    font-family:"Montserrat",sans-serif;font-weight:800;font-size:21px;line-height:36px}
  .units{display:grid;grid-template-columns:64px 66px 67px 85px 1fr;gap:2px;margin-top:2px}
  .units span{background:var(--cell);height:37px;display:flex;align-items:center;padding-left:6px;font-size:8px;line-height:1.15}
  .units .alt span{background:var(--cell-alt)}
  .row{display:contents}
  .units .floor{font-size:10px}
  .units .area{font-size:15px;padding-left:10px}
  .units .price{justify-content:center}
  .row:nth-child(odd) span{background:var(--cell-alt)}

  .footer{position:absolute;left:0;top:718px;width:1200px;height:89px}
  .gallery{position:absolute;left:0;top:0;width:700px;height:80px;display:flex}
  .gallery div{flex:1}
  .g1{background:linear-gradient(135deg,#3f9fd8,#8ccaf0)}
  .g2{background:linear-gradient(135deg,#cfd2d4,#f2f2f2)}
  .g3{background:linear-gradient(135deg,#e8654a,#f6b39e)}
  .g4{background:linear-gradient(135deg,#b9c3ca,#eef0f2)}
  .contact{position:absolute;right:0;top:0;width:520px;height:80px;background:var(--blue);
    clip-path:polygon(18px 0,100% 0,100% 100%,0 100%);color:var(--white);padding-left:34px}
  .contact-line{font-size:11.5px;margin-top:17px;letter-spacing:.2px}
  .contact-url{font-family:"Montserrat",sans-serif;font-weight:800;font-size:30px;margin-top:2px;letter-spacing:.3px}
  .footer-rule{position:absolute;left:0;bottom:0;width:1200px;height:9px;background:var(--red)}
</style>
</head>
<body>

<section class="hero" role="img" aria-label="Aussenvisualisierung der Wohnanlage mit Wiese, Bäumen und Spazierweg">
  <h1 class="hero-title">Wohnhof<br>am Weiher</h1>
  <p class="hero-sub">Hochwertige und moderne Eigentumswohnungen</p>
</section>

<aside class="info">
  <div class="brand">
    <span class="brand-mark"></span>
    <div class="brand-name">BRUNNHOFER<br>LIEGENSCHAFTEN AG</div>
  </div>
  <div class="features">
    <div>
      <div class="feature"><h3>Bus und Bahn</h3><p>Lorem ipsum dolor sit amet, consectetuer adipiscing elit, sed diam nonummy nibh euismod tincidunt ut laoreet dolore</p></div>
      <div class="feature"><h3>Basel - Stadt</h3><p>nisl ut aliquip ex ea commodo consequat. Duis autem vel eum iriure dolor in hendrerit in vulputate velit esse molestie consequat, vel illum dolore eu feugiat nulla facilisis at vero eros</p></div>
      <div class="feature"><h3>AutoBahn</h3><p>nisl ut aliquip ex ea commodo consequat. Duis autem vel eum iriure dolor in hendrerit in vulputate velit esse molestie consequat, vel illum dolore eu feugiat nulla facilisis at vero eros</p></div>
    </div>
    <div>
      <div class="feature"><h3>BEinkaufen und weitere Dienstleistungen</h3><p>nisl ut aliquip ex ea commodo consequat. Duis autem vel eum iriure dolor in hendrerit in vulputate velit esse molestie consequat, vel illum dolore eu feugiat nulla facilisis at vero eros el eum iriure dolor in hendrerit in vulputate velit esse molestie c</p></div>
      <div class="feature"><h3>Erholung im Grunen</h3><p>nisl ut aliquip ex ea commodo consequat. Duis autem vel eum iriure dolor in hendrerit in vulputate velit esse molestie consequat, vel illum dolore eu feugiat nulla facilisis at vero eros</p></div>
    </div>
  </div>
  <div class="divider"></div>
  <p class="cta">Fordern Sie noch heute die Verkaufsunterlagen gedruckt oder per<br>Email an. Schreiben Sie uns einfach eine Chatpost mit Ihrer Adresse.</p>
</aside>

<div class="band"></div>

<section class="house house-a">
  <div class="house-accent"></div>
  <h2 class="house-head">Haus A</h2>
  <div class="units">
    <div class="row"><span class="floor">Attika</span><span>4.5<br>Zimmer</span><span class="area">108m²</span><span>105m2<br>Sonnenterrasse</span><span class="price">945'000 CHF</span></div>
    <div class="row"><span class="floor">Oberges<br>choss</span><span>35<br>Zimmer</span><span class="area">81m²</span><span>16m2 Balkon</span><span class="price">754'800 CHF</span></div>
    <div class="row"><span class="floor">Oberges<br>choss</span><span>4.5<br>Zimmer</span><span class="area">102m²</span><span>33m2 Balkon</span><span class="price">640'000 CHF</span></div>
    <div class="row"><span class="floor">Erdges<br>choss</span><span>3.5<br>Zimmer</span><span class="area">81m²</span><span>16m2<br>gedeckter Sitzplatz<br>&amp; eigener Garten</span><span class="price">657'000 CHF</span></div>
    <div class="row"><span class="floor">Erdges<br>choss</span><span>4.5<br>Zimmer</span><span class="area">102m²</span><span>33m2 gedeckter<br>Sitzplatz &amp; eigener<br>Garten</span><span class="price">765'000 CHF</span></div>
  </div>
</section>

<section class="house house-b">
  <div class="house-accent"></div>
  <h2 class="house-head">Haus B</h2>
  <div class="units">
    <div class="row"><span class="floor">Attika</span><span>4.5<br>Zimmer</span><span class="area">108m²</span><span>105m2<br>Sonnenterrasse</span><span class="price">945'000 CHF</span></div>
    <div class="row"><span class="floor">Oberges<br>choss</span><span>35<br>Zimmer</span><span class="area">81m²</span><span>16m2 Balkon</span><span class="price">754'800 CHF</span></div>
    <div class="row"><span class="floor">Oberges<br>choss</span><span>4.5<br>Zimmer</span><span class="area">102m²</span><span>33m2 Balkon</span><span class="price">640'000 CHF</span></div>
    <div class="row"><span class="floor">Erdges<br>choss</span><span>3.5<br>Zimmer</span><span class="area">81m²</span><span>16m2<br>gedeckter Sitzplatz<br>&amp; eigener Garten</span><span class="price">657'000 CHF</span></div>
    <div class="row"><span class="floor">Erdges<br>choss</span><span>4.5<br>Zimmer</span><span class="area">102m²</span><span>33m2 gedeckter<br>Sitzplatz &amp; eigener<br>Garten</span><span class="price">765'000 CHF</span></div>
  </div>
</section>

<section class="house house-c">
  <div class="house-accent"></div>
  <h2 class="house-head">Haus C</h2>
  <div class="units">
    <div class="row"><span class="floor">Attika</span><span>4.5<br>Zimmer</span><span class="area">108m²</span><span>105m2<br>Sonnenterrasse</span><span class="price">945'000 CHF</span></div>
    <div class="row"><span class="floor">Oberges<br>choss</span><span>35<br>Zimmer</span><span class="area">81m²</span><span>16m2 Balkon</span><span class="price">754'800 CHF</span></div>
    <div class="row"><span class="floor">Oberges<br>choss</span><span>4.5<br>Zimmer</span><span class="area">102m²</span><span>33m2 Balkon</span><span class="price">640'000 CHF</span></div>
    <div class="row"><span class="floor">Erdges<br>choss</span><span>3.5<br>Zimmer</span><span class="area">81m²</span><span>16m2<br>gedeckter Sitzplatz<br>&amp; eigener Garten</span><span class="price">657'000 CHF</span></div>
    <div class="row"><span class="floor">Erdges<br>choss</span><span>4.5<br>Zimmer</span><span class="area">102m²</span><span>33m2 gedeckter<br>Sitzplatz &amp; eigener<br>Garten</span><span class="price">765'000 CHF</span></div>
  </div>
</section>

<footer class="footer">
  <div class="gallery">
    <div class="g1" role="img" aria-label="Innenvisualisierung Wohnzimmer, blau getönt"></div>
    <div class="g2" role="img" aria-label="Innenvisualisierung Essbereich, hell"></div>
    <div class="g3" role="img" aria-label="Innenvisualisierung Wohnraum, rot getönt"></div>
    <div class="g4" role="img" aria-label="Innenvisualisierung Küche, hell"></div>
  </div>
  <div class="contact">
    <p class="contact-line">Seematteweg 14,&nbsp; 4387 Tannried &nbsp;&nbsp;|&nbsp;&nbsp; 079 462 37 58 &nbsp;&nbsp;|&nbsp;&nbsp; rbrunnhofer@tessin-ostwald.ch</p>
    <p class="contact-url">www.wohnhof-am-weiher.ch</p>
  </div>
  <div class="footer-rule"></div>
</footer>

</body>
</html>
```